Construction APP

We need to design a modern app IOS/Android where my team can create a profile with their info, (maybe share some pictures), reviews, submit time cards, show their availability, etc.

Like a taxi app but for construction. We also want to be able to assign each team member to a project manager with who they currently working. So we will also need to be able to create profiles at the Administration level.

The goal is to keep innovating the app as we grow, so we are always open to suggestions and ideas.

Low design quality

Industry/Entity Type

Construction

Colors
FFC000
F8CF3A
FAE287
FDF2CF
FEFAEE

Requirements
Must have
• IOS/Android APP where my team can create a profile with their info, (maybe share some pictures), reviews, submit time cards, show their availability, etc.We also want to be able to assign each team member to a project manager with who they currently working. So we will also need to be able to create profiles at the Administration level.

```html
<!DOCTYPE html>
<html lang="en">
<head>
<meta charset="UTF-8">
<title>Mr. Valmont – Onboarding Screens</title>
<link href="https://fonts.googleapis.com/css2?family=Inter:wght@400;500;600;700&display=swap" rel="stylesheet">
<style>
  :root {
    --canvas-bg: #f4f4f4;
    --screen-bg: #ffffff;
    --ink: #1c1c1c;
    --ink-soft: #333333;
    --button-grey: #f4f4f4;
    --code-box: #fafafa;
    --code-border: #eeeeee;
    --brand-yellow: #ffc000;
    --shadow: rgba(160, 180, 200, 0.35);
  }
  * { box-sizing: border-box; margin: 0; padding: 0; }
  html, body {
    width: 1200px; height: 1000px; overflow: hidden;
    background: var(--canvas-bg);
    font-family: "Inter", sans-serif;
    color: var(--ink);
  }
  .board { position: relative; width: 1200px; height: 1000px; }

  .screen {
    position: absolute; top: 113px; width: 356px; height: 774px;
    background: var(--screen-bg); border-radius: 22px;
    box-shadow: 0 18px 40px var(--shadow);
    overflow: hidden;
  }
  .screen--splash { left: 28px; }
  .screen--welcome { left: 422px; }
  .screen--admin { left: 816px; }

  .status-bar {
    position: absolute; top: 12px; left: 21px; right: 14px; height: 20px;
    display: flex; justify-content: space-between; align-items: center;
  }
  .status-bar__time { font-size: 15px; font-weight: 600; }
  .status-bar__icons { display: flex; gap: 5px; align-items: center; }

  .home-indicator {
    position: absolute; bottom: 8px; left: 121px; width: 115px; height: 4px;
    border-radius: 2px; background: var(--ink);
  }

  .brand-lockup {
    position: absolute; top: 410px; left: 0; right: 0;
    display: flex; justify-content: center; align-items: center; gap: 10px;
  }
  .brand-lockup__mark { width: 22px; height: 22px; background: var(--ink); }
  .brand-lockup__name {
    font-size: 34px; font-weight: 700; letter-spacing: -0.5px; color: var(--ink);
  }

  .screen-title {
    position: absolute; left: 17px;
    font-size: 31px; font-weight: 700; line-height: 38px; letter-spacing: -0.3px;
  }
  .screen--welcome .screen-title { top: 158px; }
  .screen--admin .screen-title { top: 118px; }

  .role-button {
    position: absolute; left: 40px; width: 276px; height: 56px;
    background: var(--button-grey); border-radius: 3px;
    display: flex; justify-content: center; align-items: center;
    font-size: 20px; font-weight: 500;
  }
  .role-button--admin { top: 391px; }
  .role-button--worker { top: 487px; }

  .admin-hint {
    position: absolute; left: 23px; top: 289px;
    font-size: 16px; color: var(--ink-soft);
  }
  .code-label {
    position: absolute; left: 0; right: 0; top: 379px; text-align: center;
    font-size: 18px; font-weight: 600;
  }
  .code-inputs {
    position: absolute; left: 16px; top: 452px; display: flex; gap: 11px;
  }
  .code-inputs__cell {
    position: relative; width: 56px; height: 62px;
    background: var(--code-box); border: 1px solid var(--code-border);
  }
  .code-inputs__cell::after {
    content: ""; position: absolute; left: 16px; bottom: 8px;
    width: 24px; height: 1.5px; background: var(--ink);
  }
  .forgot-link {
    position: absolute; right: 16px; top: 535px;
    font-size: 14px; color: var(--ink-soft);
  }
  .confirm-button {
    position: absolute; left: 40px; top: 658px; width: 276px; height: 56px;
    background: var(--brand-yellow); border-radius: 3px;
    display: flex; justify-content: center; align-items: center;
    font-size: 20px; font-weight: 600;
  }
</style>
</head>
<body>
<main class="board">

  <section class="screen screen--splash">
    <div class="brand-lockup">
      <span class="brand-lockup__mark"></span>
      <span class="brand-lockup__name">MR. VALMONT</span>
    </div>
  </section>

  <section class="screen screen--welcome">
    <div class="status-bar">
      <span class="status-bar__time">9:41</span>
      <span class="status-bar__icons">
        <svg width="18" height="11" viewBox="0 0 18 11"><rect x="0" y="7" width="3" height="4" rx="0.5" fill="#1c1c1c"/><rect x="5" y="5" width="3" height="6" rx="0.5" fill="#1c1c1c"/><rect x="10" y="2.5" width="3" height="8.5" rx="0.5" fill="#1c1c1c"/><rect x="15" y="0" width="3" height="11" rx="0.5" fill="#1c1c1c"/></svg>
        <svg width="16" height="11" viewBox="0 0 16 11"><path d="M8 10.5 L10.3 8 A3.3 3.3 0 0 0 5.7 8 Z" fill="#1c1c1c"/><path d="M3.6 5.9 A6.2 6.2 0 0 1 12.4 5.9" stroke="#1c1c1c" stroke-width="1.8" fill="none"/><path d="M1 3.3 A9.8 9.8 0 0 1 15 3.3" stroke="#1c1c1c" stroke-width="1.8" fill="none"/></svg>
        <svg width="25" height="12" viewBox="0 0 25 12"><rect x="0.5" y="0.5" width="21" height="11" rx="3" stroke="#1c1c1c" fill="none" opacity="0.4"/><rect x="2" y="2" width="18" height="8" rx="1.8" fill="#1c1c1c"/><rect x="23" y="4" width="1.5" height="4" rx="0.7" fill="#1c1c1c" opacity="0.4"/></svg>
      </span>
    </div>
    <h1 class="screen-title">Hi! Welcome to<br>Mr. Valmont</h1>
    <div class="role-button role-button--admin">Admin</div>
    <div class="role-button role-button--worker">Worker</div>
    <span class="home-indicator"></span>
  </section>

  <section class="screen screen--admin">
    <div class="status-bar">
      <span class="status-bar__time">9:41</span>
      <span class="status-bar__icons">
        <svg width="18" height="11" viewBox="0 0 18 11"><rect x="0" y="7" width="3" height="4" rx="0.5" fill="#1c1c1c"/><rect x="5" y="5" width="3" height="6" rx="0.5" fill="#1c1c1c"/><rect x="10" y="2.5" width="3" height="8.5" rx="0.5" fill="#1c1c1c"/><rect x="15" y="0" width="3" height="11" rx="0.5" fill="#1c1c1c"/></svg>
        <svg width="16" height="11" viewBox="0 0 16 11"><path d="M8 10.5 L10.3 8 A3.3 3.3 0 0 0 5.7 8 Z" fill="#1c1c1c"/><path d="M3.6 5.9 A6.2 6.2 0 0 1 12.4 5.9" stroke="#1c1c1c" stroke-width="1.8" fill="none"/><path d="M1 3.3 A9.8 9.8 0 0 1 15 3.3" stroke="#1c1c1c" stroke-width="1.8" fill="none"/></svg>
        <svg width="25" height="12" viewBox="0 0 25 12"><rect x="0.5" y="0.5" width="21" height="11" rx="3" stroke="#1c1c1c" fill="none" opacity="0.4"/><rect x="2" y="2" width="18" height="8" rx="1.8" fill="#1c1c1c"/><rect x="23" y="4" width="1.5" height="4" rx="0.7" fill="#1c1c1c" opacity="0.4"/></svg>
      </span>
    </div>
    <h1 class="screen-title">Hi! Admin</h1>
    <p class="admin-hint">Enter your admin code to continue...</p>
    <p class="code-label">Enter the numeric code</p>
    <div class="code-inputs">
      <span class="code-inputs__cell"></span>
      <span class="code-inputs__cell"></span>
      <span class="code-inputs__cell"></span>
      <span class="code-inputs__cell"></span>
      <span class="code-inputs__cell"></span>
    </div>
    <span class="forgot-link">Forgot your code?</span>
    <div class="confirm-button">Confirm</div>
    <span class="home-indicator"></span>
  </section>

</main>
</body>
</html>
```